Cradle Glow Events

New Company ,I will attened clients personal residents(venu of there choice) and provide 3D ultra sound photos at time of ultra sound.This is a Non diagnostic ultra sound which does not replace the ultrasound reqested by Dr.The best time for ultra sound is 24 to 34 weeks.The baby sex can be kept confidential if requied and all cultral and diverse backgrounds cattered for..No referal requied for this.I have 2 main packges,1 baby shower and 2 family time.Extra options available are entertainment,Family time prior to baby shower for dad,decoration, Kids entertainment.
Contact number is 0471938402 email to be added ASAP.
prices start from $450

It Company

```html
<!DOCTYPE html>
<html lang="en">
<head>
<meta charset="utf-8">
<title>Cradle Glow Events – Flyer</title>
<link href="https://fonts.googleapis.com/css2?family=Montserrat:wght@600;700;800&family=Questrial&display=swap" rel="stylesheet">
<style>
  :root {
    --magenta: #c7245e;
    --plum: #8e2a6e;
    --orange: #f06a27;
    --ink: #111111;
    --paper: #ffffff;
    --skin-light: #f3e6df;
    --skin-mid: #e2c8bb;
    --clinic: #d9dde2;
    --scan-dark: #5a2a10;
    --scan-light: #d9873e;
  }
  * { margin: 0; padding: 0; box-sizing: border-box; }
  html, body { width: 816px; height: 1200px; overflow: hidden; background: var(--paper); }
  .flyer { position: relative; width: 816px; height: 1200px; overflow: hidden; background: var(--paper); font-family: "Questrial", sans-serif; }

  .clinic-photo {
    position: absolute; left: 0; top: 0; width: 816px; height: 420px;
    background: linear-gradient(160deg, var(--clinic) 0%, #eef0f2 45%, var(--skin-mid) 75%, var(--skin-light) 100%);
  }
  .belly-photo {
    position: absolute; left: 0; top: 400px; width: 420px; height: 800px;
    background: radial-gradient(ellipse at 20% 60%, var(--skin-mid) 0%, var(--skin-light) 55%, rgba(255,255,255,0) 85%);
  }
  .scan-strip {
    position: absolute; left: 22px; top: 610px; width: 230px; height: 545px;
    background: #fbfaf8; transform: rotate(-3deg); padding: 14px;
    display: flex; flex-direction: column; gap: 14px;
    box-shadow: 0 2px 6px rgba(0,0,0,0.2);
  }
  .scan-frame { flex: 1; background: radial-gradient(ellipse at 50% 45%, var(--scan-light) 0%, #a75522 55%, var(--scan-dark) 100%); }

  .waves { position: absolute; left: 0; top: 320px; width: 816px; height: 130px; }

  .brand {
    position: absolute; left: 250px; top: 130px; width: 400px;
    display: flex; align-items: center; gap: 14px;
  }
  .brand-dot { width: 22px; height: 22px; border-radius: 50%; background: var(--magenta); flex: none; }
  .brand-name { font-family: "Montserrat", sans-serif; font-weight: 700; font-size: 44px; line-height: 1.05; color: var(--magenta); }

  .intro {
    position: absolute; left: 430px; top: 428px; width: 376px;
    font-size: 18.6px; line-height: 23px; color: var(--magenta);
  }

  .packages { position: absolute; left: 430px; top: 676px; width: 376px; text-align: center; font-family: "Montserrat", sans-serif; }
  .packages h2 { font-weight: 800; line-height: 1.1; }
  .packages ul { list-style: none; }
  .packages li { font-weight: 600; text-transform: uppercase; line-height: 1.1; }
  .main-title { font-size: 30px; color: var(--orange); }
  .main-list li { font-size: 23px; color: var(--orange); margin-top: 9px; }
  .extra-title { font-size: 28px; color: var(--magenta); margin-top: 12px; }
  .extra-list li { font-size: 19px; color: var(--magenta); margin-top: 13px; }
  .extra-list li.two-line { line-height: 1.2; }

  .contact { position: absolute; left: 300px; top: 990px; width: 520px; text-align: center; font-family: "Montserrat", sans-serif; font-weight: 800; color: var(--ink); font-size: 27px; line-height: 40px; }

  .price { position: absolute; left: 300px; top: 1070px; width: 500px; height: 104px; font-family: "Montserrat", sans-serif; }
  .price-label { position: absolute; left: 6px; top: 30px; font-weight: 800; font-size: 33px; color: var(--magenta); }
  .price-badge {
    position: absolute; left: 350px; top: 0; width: 114px; height: 104px; border-radius: 50%;
    background: var(--plum); color: var(--paper); font-weight: 800;
    display: flex; align-items: center; justify-content: center; font-size: 40px;
  }
  .price-badge sup { font-size: 20px; margin-right: 2px; }
</style>
</head>
<body>
<main class="flyer">
  <div class="clinic-photo" role="img" aria-label="Photo of a sonographer holding an ultrasound probe over a pregnant belly in a clinic"></div>
  <div class="belly-photo" role="img" aria-label="Photo of a pregnant belly with a hand holding an ultrasound print strip"></div>
  <div class="scan-strip" role="img" aria-label="Strip of three 3D ultrasound baby images">
    <div class="scan-frame"></div>
    <div class="scan-frame"></div>
    <div class="scan-frame"></div>
  </div>

  <svg class="waves" viewBox="0 0 816 130" preserveAspectRatio="none" aria-hidden="true">
    <path d="M0 40 C 220 -10, 520 -5, 816 20 L816 48 C 520 20, 240 25, 0 80 Z" fill="var(--plum)"/>
    <path d="M0 70 C 240 20, 520 20, 816 40 L816 78 C 520 55, 250 62, 0 108 Z" fill="var(--magenta)"/>
    <path d="M0 104 C 250 58, 520 52, 816 74 L816 86 C 520 68, 260 76, 0 118 Z" fill="var(--orange)"/>
    <path d="M0 118 C 260 76, 520 68, 816 86 L816 130 L0 130 Z" fill="var(--paper)"/>
  </svg>

  <div class="brand">
    <span class="brand-dot"></span>
    <h1 class="brand-name">Cradle Glow Events</h1>
  </div>

  <p class="intro">A Non diagnostic ultra sound which does not replace the ultrasound reqested by Dr. The best time for ultra sound is 24 to 34 weeks. The baby sex can be kept confidential if required and all cultral and diverse backgrounds cattered for..No referal required for this.&nbsp; Cradle Glow Events is a mobile service and will attend to the venue of your choice.</p>

  <section class="packages">
    <h2 class="main-title">MAIN PACKAGES</h2>
    <ul class="main-list">
      <li>Baby Shower</li>
      <li>Family Time</li>
    </ul>
    <h2 class="extra-title">EXTRA PACKAGES</h2>
    <ul class="extra-list">
      <li>Entertainment</li>
      <li class="two-line">Family time prior to<br>baby shower for dad</li>
      <li>Decoration</li>
      <li>Kids entertainment.</li>
    </ul>
  </section>

  <div class="contact">
    <p>CALL 0471938402</p>
    <p>OR EMAIL ----@MAILNEST.COM</p>
  </div>

  <div class="price">
    <span class="price-label">PRICES START AT</span>
    <span class="price-badge"><sup>$</sup>450</span>
  </div>
</main>
</body>
</html>
```